Letter Head- Window Cleaning Industry

Need a letter head for 'Brindlecove Window Cleaning'. We provide a premium residential & commercial window cleaning service to Melbourne and surrounding suburbs.
Would like a design similar to the flyer, logo and uniform attached. The final design should communicate trust and quality.
Address is 2304/18 Tamsworth St, Kelbury Victoria 3214. The rest of the information is on the flyer.
*Please note the Phone number on the uniform designs is incorrect.

Thank-you very much!

Industry/Entity Type

Window Cleaning

```html
<!DOCTYPE html>
<html lang="en">
<head>
<meta charset="utf-8">
<title>Brindlecove Window Cleaning – Letterhead</title>
<link rel="stylesheet" href="https://fonts.googleapis.com/css2?family=Didact+Gothic&display=swap">
<style>
  :root {
    --paper: #ffffff;
    --ink: #6d6d6d;
    --ink-soft: #8a8a8a;
    --rule: #9a9a9a;
    --brand: #ee8a2c;
    --skyline: #f1f1f1;
    --skyline-fade: #fafafa;
  }
  html, body {
    margin: 0;
    padding: 0;
    overflow: hidden;
    background: var(--paper);
  }
  .letterhead {
    position: relative;
    width: 927px;
    height: 1200px;
    overflow: hidden;
    background: var(--paper);
    font-family: "Didact Gothic", "Century Gothic", sans-serif;
    color: var(--ink);
  }
  .brand-name {
    position: absolute;
    top: 22px;
    left: 0;
    width: 100%;
    margin: 0;
    text-align: center;
    font-size: 44px;
    font-weight: 400;
    letter-spacing: 0.5px;
    color: var(--brand);
  }
  .address-block {
    position: absolute;
    top: 104px;
    left: 0;
    width: 100%;
    text-align: center;
  }
  .address-line {
    font-size: 15px;
    color: var(--ink);
    margin: 0;
    line-height: 20px;
  }
  .address-city {
    font-size: 14px;
    letter-spacing: 5px;
    color: var(--ink);
    margin: 0;
    line-height: 18px;
    word-spacing: 14px;
  }
  .rule {
    position: absolute;
    height: 1px;
    background: var(--rule);
  }
  .rule--head-left { top: 124px; left: 0; width: 297px; }
  .rule--head-right { top: 124px; left: 628px; width: 299px; }
  .skyline {
    position: absolute;
    left: 0;
    top: 710px;
    width: 927px;
    height: 465px;
  }
  .watermark-name {
    position: absolute;
    top: 1058px;
    left: 0;
    width: 100%;
    margin: 0;
    text-align: center;
    font-size: 96px;
    font-weight: 400;
    letter-spacing: 2px;
    color: var(--paper);
    line-height: 1;
  }
  .contact-bar {
    position: absolute;
    top: 1166px;
    left: 0;
    width: 100%;
    display: flex;
    justify-content: center;
    align-items: center;
    gap: 30px;
    font-size: 14.5px;
    color: var(--ink-soft);
  }
  .rule--foot-left { top: 1176px; left: 0; width: 128px; }
  .rule--foot-right { top: 1176px; left: 802px; width: 125px; }
</style>
</head>
<body>
<main class="letterhead">
  <h1 class="brand-name">Brindlecove Window Cleaning</h1>

  <div class="rule rule--head-left"></div>
  <div class="address-block">
    <p class="address-line">2304/18 Tamsworth St, Kelbury Victoria 3214</p>
    <p class="address-city">MELBOURNE - AUSTRALIA</p>
  </div>
  <div class="rule rule--head-right"></div>

  <svg class="skyline" viewBox="0 0 927 465" role="img" aria-label="Faint grey silhouette of the Melbourne city skyline">
    <defs>
      <linearGradient id="skylineTone" x1="0" y1="0" x2="0" y2="1">
        <stop offset="0" stop-color="var(--skyline-fade)"/>
        <stop offset="0.4" stop-color="var(--skyline)"/>
        <stop offset="1" stop-color="var(--skyline)"/>
      </linearGradient>
    </defs>
    <rect x="0" y="0" width="927" height="465" fill="url(#skylineTone)"/>
  </svg>

  <p class="watermark-name">BRINDLECOVE</p>

  <div class="rule rule--foot-left"></div>
  <div class="contact-bar">
    <span class="contact-web">brindlecovewindows.com.au</span>
    <span class="contact-sep">-</span>
    <span class="contact-email">info@brindlecovewindows.com.au</span>
    <span class="contact-sep">-</span>
    <span class="contact-phone">T: 8412 3957</span>
  </div>
  <div class="rule rule--foot-right"></div>
</main>
</body>
</html>
```